Darrow Consulting needs a quality & professional business card!

I am a recruitment and employment consultant from Brisbane, Australia and I had a fantastic logo organised by this community to I am hoping the business card will be the same.

I have attached the Darrow consulting logo that ideally would feature on the back of the business card. There are a number of logos for you to use as you see fit. I would like the colour cheme to match that of the Darrow Consulting logo. I also have a secondary company called Career Lantern Australia and I have included that logo as well. While it is an important part of the business I don't want this logo feature too predominantly as I am moving out of this space. This logo was created by myself and is of low quality. Feel free to use the icon and words however you want. The winning design will be smart, professional and eye-catching.

The information I am looking for in the business card is:
Name: Gavin Darrow
Position: Founder & Director
Phone: (07) 3519 6482
Mobile: 0431 586 207
Email: gavin@careerlantern.com.au

Target Market(s)

Recruiters, government, large companies

Contact Information for Business Card

Name: Gavin Darrow
Phone: (07) 3519 6482
Mobile: 0431 586 207
Web: www.careerlantern.com.au

Font styles to use
Serif
Sans Serif

Requirements
Must have
• Darrow Consulting Logo on reverse side
• Contact details on front side with smaller reference to Darrow Consulting logo and Career Lantern Australia logo

```html
<!DOCTYPE html>
<html lang="en">
<head>
<meta charset="utf-8">
<title>Gavin Darrow – Business Card</title>
<link href="https://fonts.googleapis.com/css2?family=Montserrat:wght@400;600;700&display=swap" rel="stylesheet">
<style>
  :root {
    --orange: #e08a3a;
    --green: #1fad55;
    --blue: #1793cc;
    --white: #ffffff;
    --name-red: #d4262e;
    --title-orange: #ea6428;
    --ink: #1e1e1e;
  }
  html, body {
    margin: 0;
    padding: 0;
    overflow: hidden;
    background: #ffffff;
  }
  .card {
    position: relative;
    width: 1200px;
    height: 667px;
    overflow: hidden;
    font-family: "Montserrat", Arial, sans-serif;
    color: var(--white);
  }
  .card-art {
    position: absolute;
    inset: 0;
  }
  .contact-label,
  .contact-value {
    position: absolute;
    left: 212px;
    margin: 0;
    white-space: nowrap;
    line-height: 1;
  }
  .contact-label {
    font-weight: 700;
    font-size: 41px;
  }
  .contact-value {
    font-weight: 400;
    font-size: 38px;
  }
  .phone-label  { top: 60px; }
  .phone-value  { top: 117px; }
  .mobile-label { top: 296px; }
  .mobile-value { top: 347px; }
  .email-label  { top: 528px; }
  .email-value  { top: 568px; }

  .identity {
    position: absolute;
    left: 712px;
    top: 228px;
    width: 440px;
    text-align: center;
  }
  .person-name {
    margin: 0;
    font-weight: 700;
    font-size: 56px;
    line-height: 1;
    color: var(--name-red);
    letter-spacing: 0.5px;
    white-space: nowrap;
  }
  .person-title {
    margin: 8px 0 0;
    font-weight: 400;
    font-size: 44px;
    line-height: 1;
    color: var(--title-orange);
    white-space: nowrap;
  }
  .brand-row {
    position: absolute;
    top: 360px;
    left: 832px;
    display: flex;
    align-items: center;
    gap: 26px;
  }
  .brand {
    display: flex;
    align-items: center;
    gap: 6px;
    font-weight: 600;
    font-size: 15px;
    color: var(--ink);
    white-space: nowrap;
  }
  .brand-dot {
    width: 26px;
    height: 26px;
    border-radius: 50%;
    background: var(--ink);
  }
  .brand-square {
    width: 24px;
    height: 24px;
    background: var(--ink);
  }
</style>
</head>
<body>
<div class="card">
  <svg class="card-art" width="1200" height="667" viewBox="0 0 1200 667" aria-hidden="true">
    <rect class="band-phone" x="0" y="0" width="1200" height="226" fill="var(--orange)"/>
    <rect class="band-mobile" x="0" y="226" width="1200" height="229" fill="var(--green)"/>
    <rect class="band-email" x="0" y="455" width="1200" height="212" fill="var(--blue)"/>
    <path class="name-panel" fill="var(--white)"
          d="M1067 0 H1200 V667 H1067 L782 506 Q689 452 689 333 Q689 214 782 160 Z"/>
    <g class="edge-stripe">
      <rect x="1166" y="135" width="18" height="183" fill="var(--orange)"/>
      <rect x="1166" y="318" width="18" height="156" fill="var(--green)"/>
      <rect x="1166" y="474" width="18" height="26" fill="var(--blue)"/>
    </g>

    <!-- phone handset icon -->
    <g class="icon-phone" fill="var(--white)">
      <path d="M52 44 L76 32 L100 80 L82 94 Q96 124 126 140 L142 124 L174 146 L160 168
               Q140 180 108 162 Q62 134 44 88 Q36 62 52 44 Z"/>
      <path d="M80 28 L88 24 L110 70 L102 76 Z"/>
      <path d="M148 118 L154 112 L178 132 L172 140 Z"/>
    </g>

    <!-- mobile icon -->
    <g class="icon-mobile">
      <rect x="54" y="249" width="87" height="157" rx="12" fill="var(--white)"/>
      <rect x="62" y="262" width="71" height="127" rx="6" fill="var(--green)"/>
      <rect x="84" y="256" width="27" height="8" rx="3" fill="var(--white)"/>
    </g>

    <!-- envelope icon -->
    <g class="icon-email">
      <rect x="34" y="511" width="135" height="93" rx="16" fill="var(--white)"/>
      <path d="M58 524 H146 Q156 524 148 532 L108 566 Q102 571 96 566 L56 532 Q48 524 58 524 Z"
            fill="none" stroke="var(--blue)" stroke-width="6" stroke-linejoin="round"/>
    </g>
  </svg>

  <p class="contact-label phone-label">Phone</p>
  <p class="contact-value phone-value">(07) 3519 6482</p>

  <p class="contact-label mobile-label">Mobile</p>
  <p class="contact-value mobile-value">0431 586 207</p>

  <p class="contact-label email-label">E -Mail</p>
  <p class="contact-value email-value">gavin@careerlantern.com.au</p>

  <div class="identity">
    <h1 class="person-name">Gavin Darrow</h1>
    <p class="person-title">Founder &amp; Director</p>
  </div>

  <div class="brand-row">
    <span class="brand brand-career-lantern"><span class="brand-dot"></span>Career Lantern</span>
    <span class="brand brand-darrow"><span class="brand-square"></span>Darrow Consulting</span>
  </div>
</div>
</body>
</html>
```